Business Card and Stationary for Brantley Consulting
Brantley Consulting
Business Card and Stationary for Brantley Consulting - Energy
Creative Brief
Professional
Dale Pruitt
Inspector
17 Juniper Court Red Deer Alberta, Canada T4P 2K9
dale_pruitt@mailvora.com
brantleyconsulting brantleyconsulting
2 sided business card and stationary design. Let's see what you got.

```html
<!DOCTYPE html>
<html lang="en">
<head>
<meta charset="utf-8">
<title>Brantley Consulting – Business Card</title>
<link rel="stylesheet" href="https://fonts.googleapis.com/css2?family=Montserrat:wght@400;600;800&display=swap">
<style>
  :root {
    --stage: #2a2a2c;
    --card: #0a0a0b;
    --brand-blue: #1f8fe6;
    --blue-deep: #0d4fb3;
    --blue-light: #3ec0ff;
    --silver: #c9ccd1;
    --text-light: #e9eaec;
    --text-muted: #a9acb2;
  }
  * { margin: 0; padding: 0; box-sizing: border-box; }
  html, body {
    width: 1200px; height: 802px; overflow: hidden;
    background: var(--stage);
    font-family: "Montserrat", Arial, sans-serif;
  }
  .stage {
    position: relative; width: 1200px; height: 802px;
    display: flex; align-items: center; justify-content: center; gap: 60px;
  }
  .card {
    position: relative; width: 520px; height: 297px;
    background: var(--card); overflow: hidden;
    box-shadow: 0 10px 30px rgba(0,0,0,.5);
  }
  .swoosh { position: absolute; left: 0; bottom: 0; width: 520px; height: 100px; }
  .website {
    position: absolute; left: 36px; bottom: 14px;
    color: var(--text-light); font-size: 11px; font-weight: 600; letter-spacing: .3px;
  }
  .brand {
    display: flex; align-items: center; gap: 8px;
    color: var(--brand-blue); font-weight: 800; text-transform: uppercase;
  }
  .brand-dot { border-radius: 50%; background: var(--brand-blue); flex: none; }
  .card-back .brand { position: absolute; left: 30px; top: 34px; font-size: 15px; letter-spacing: .5px; }
  .card-back .brand-dot { width: 14px; height: 14px; }
  .contact-list { position: absolute; left: 30px; top: 90px; list-style: none; }
  .contact-list li {
    display: flex; align-items: center; gap: 8px;
    color: var(--text-muted); font-size: 8.5px; height: 15px;
  }
  .contact-list svg { width: 9px; height: 9px; fill: var(--text-light); flex: none; }
  .person { position: absolute; right: 34px; top: 108px; text-align: right; }
  .person-name { color: var(--text-light); font-size: 13px; font-weight: 600; letter-spacing: 1px; text-transform: uppercase; }
  .person-title { color: var(--text-muted); font-size: 8.5px; margin-top: 3px; }
  .divider {
    position: absolute; left: 150px; right: 30px; top: 146px; height: 1px;
    background: linear-gradient(90deg, transparent, var(--silver));
  }
  .address {
    position: absolute; right: 34px; top: 172px; text-align: right;
    color: var(--text-muted); font-size: 8.5px; line-height: 13px;
  }
  .card-front .brand {
    position: absolute; left: 0; right: 0; top: 112px; justify-content: center;
    font-size: 24px; letter-spacing: 1px;
  }
  .card-front .brand-dot { width: 22px; height: 22px; }
</style>
</head>
<body>
<main class="stage">

  <section class="card card-back" aria-label="Business card, contact side">
    <div class="brand"><span class="brand-dot"></span>Brantley Consulting</div>

    <ul class="contact-list">
      <li><svg viewBox="0 0 10 10"><path d="M2 0.5 3.6 2.6 2.8 3.6C3.5 5 4.9 6.4 6.3 7.1L7.4 6.3 9.5 8 8.5 9.5C4.5 9.5.5 5.5.5 1.5Z"/></svg>012 345 6789</li>
      <li><svg viewBox="0 0 10 10"><path d="M2 0.5 3.6 2.6 2.8 3.6C3.5 5 4.9 6.4 6.3 7.1L7.4 6.3 9.5 8 8.5 9.5C4.5 9.5.5 5.5.5 1.5Z"/></svg>012 345 6789</li>
      <li><svg viewBox="0 0 10 10"><path d="M3 0h4a1 1 0 0 1 1 1v8a1 1 0 0 1-1 1H3a1 1 0 0 1-1-1V1a1 1 0 0 1 1-1Zm0 1.5v6h4v-6Z"/></svg>012 345 6789</li>
      <li><svg viewBox="0 0 10 10"><path d="M0 2h10v6H0Zm1 1v.4l4 2.6 4-2.6V3L5 5.4Z"/></svg>dale_pruitt@mailvora.com</li>
      <li><svg viewBox="0 0 10 10"><path d="M5 0a5 5 0 1 0 0 10A5 5 0 0 0 5 0Zm0 1c.7.6 1.2 1.9 1.3 3.5H3.7C3.8 2.9 4.3 1.6 5 1ZM1 5.5h1.7c.1 1.3.4 2.4.9 3.2A4 4 0 0 1 1 5.5Zm0-1a4 4 0 0 1 2.6-3.2c-.5.8-.8 1.9-.9 3.2Zm2.7 1h2.6C6.2 7.1 5.7 8.4 5 9c-.7-.6-1.2-1.9-1.3-3.5Zm3.6 0H9a4 4 0 0 1-2.6 3.2c.5-.8.8-1.9.9-3.2Zm0-1c-.1-1.3-.4-2.4-.9-3.2A4 4 0 0 1 9 4.5Z"/></svg>www.brantleyconsulting.com</li>
    </ul>

    <div class="person">
      <p class="person-name">Dale Pruitt</p>
      <p class="person-title">Managing Director</p>
    </div>
    <div class="divider"></div>
    <p class="address">17 Juniper Court<br>Red Deer AB</p>

    <svg class="swoosh" viewBox="0 0 520 100" preserveAspectRatio="none" aria-hidden="true">
      <defs>
        <linearGradient id="blueBandBack" x1="0" y1="0" x2="1" y2="0">
          <stop offset="0" stop-color="#0d4fb3"/>
          <stop offset=".6" stop-color="#1f8fe6"/>
          <stop offset="1" stop-color="#3ec0ff"/>
        </linearGradient>
      </defs>
      <path d="M0 62C140 44 320 44 520 8V100H0Z" fill="url(#blueBandBack)"/>
      <path d="M0 58C140 40 320 40 520 4" fill="none" stroke="#c9ccd1" stroke-width="3"/>
    </svg>
    <p class="website">www.brantleyconsulting.com</p>
  </section>

  <section class="card card-front" aria-label="Business card, logo side">
    <div class="brand"><span class="brand-dot"></span>Brantley Consulting</div>

    <svg class="swoosh" viewBox="0 0 520 100" preserveAspectRatio="none" aria-hidden="true">
      <defs>
        <linearGradient id="blueBandFront" x1="0" y1="0" x2="1" y2="0">
          <stop offset="0" stop-color="#0d4fb3"/>
          <stop offset=".6" stop-color="#1f8fe6"/>
          <stop offset="1" stop-color="#3ec0ff"/>
        </linearGradient>
      </defs>
      <path d="M0 62C140 44 320 44 520 8V100H0Z" fill="url(#blueBandFront)"/>
      <path d="M0 58C140 40 320 40 520 4" fill="none" stroke="#c9ccd1" stroke-width="3"/>
    </svg>
    <p class="website">www.brantleyconsulting.com</p>
  </section>

</main>
</body>
</html>
```